Create a wine label for our soon to be released Sparkling Wine

As we are about to release our new Sparkling Wine we are in need of a new label. Dimensions and text as per attached file, the design is more or less free style, but keep it a classic sparkling wine label. Keep it clean. Bottle will be near to black with black/silver cap You can use Script Font. No green, red or gold colours. We like black and silver, but don't be afraid to use some color somewhere (we can always change that). We thought of printing our logo in silver foil so a black label would be nice.

Target Market(s)

wine industry

Font styles to use
Script
Other font styles liked:
• GaramITC

Requirements
Must have
• Dimensions and text as per attached file
Nice to have
• Classic wine label
Should not have
• No gold or red or green colour

```html
<!DOCTYPE html>
<html lang="en">
<head>
<meta charset="utf-8">
<title>Frostmere Vintage Sparkling Label</title>
<link rel="stylesheet" href="https://fonts.googleapis.com/css2?family=IM+Fell+English&family=IM+Fell+English+SC&display=swap">
<style>
  :root {
    --page: #f4f3f1;
    --paper-light: #2e2f32;
    --paper-mid: #1f2022;
    --paper-deep: #111113;
    --silver: #c8ccd2;
    --silver-soft: #a9aeb5;
  }
  html, body {
    margin: 0;
    padding: 0;
    width: 960px;
    height: 1200px;
    overflow: hidden;
    background: var(--page);
  }
  .canvas {
    position: relative;
    width: 960px;
    height: 1200px;
    background: var(--page);
  }
  .label {
    position: absolute;
    left: 100px;
    top: 220px;
    width: 760px;
    height: 760px;
    overflow: hidden;
  }
  .label-art {
    position: absolute;
    inset: 0;
    width: 100%;
    height: 100%;
  }
  .brand {
    position: absolute;
    right: 40px;
    top: 62px;
    margin: 0;
    font-family: "IM Fell English SC", "IM Fell English", serif;
    font-weight: 400;
    font-size: 132px;
    line-height: 1;
    letter-spacing: 3px;
    color: var(--silver);
  }
  .region {
    position: absolute;
    right: 44px;
    top: 212px;
    margin: 0;
    font-family: "IM Fell English", serif;
    font-size: 36px;
    line-height: 1;
    letter-spacing: 2px;
    color: var(--silver);
  }
  .details {
    position: absolute;
    left: 0;
    width: 760px;
    top: 510px;
    text-align: center;
    font-family: "IM Fell English", serif;
    color: var(--silver-soft);
  }
  .vintage-year {
    margin: 0;
    font-size: 38px;
    letter-spacing: 3px;
    line-height: 1.2;
  }
  .wine-style {
    margin: 6px 0 0;
    font-size: 35px;
    line-height: 1.45;
    letter-spacing: 1px;
  }
  .method {
    margin: 34px 0 0;
    font-size: 25px;
    letter-spacing: 1px;
  }
</style>
</head>
<body>
<main class="canvas">
  <section class="label">
    <svg class="label-art" viewBox="0 0 760 760" role="img" aria-label="Dark textured paper with a pencil-sketched river winding through a landscape">
      <defs>
        <radialGradient id="paperGlow" cx="50%" cy="45%" r="70%">
          <stop offset="0%" stop-color="var(--paper-light)"/>
          <stop offset="65%" stop-color="var(--paper-mid)"/>
          <stop offset="100%" stop-color="var(--paper-deep)"/>
        </radialGradient>
      </defs>
      <rect width="760" height="760" fill="url(#paperGlow)"/>
    </svg>
    <h1 class="brand">Frostmere</h1>
    <p class="region">Tasmania</p>
    <div class="details">
      <p class="vintage-year">2013</p>
      <p class="wine-style">Vintage Sparkling<br>Blanc de Noir</p>
      <p class="method">Méthode Traditionnelle</p>
    </div>
  </section>
</main>
</body>
</html>
```